Offers of the Week

I need a blog design for a new page that will showcase the best offers available in grocery retail and restaurants.

Key features I am looking for in design:
I need to post a video at top of page
I want separate button features so viewer can go straight to retail, grocery or restaurant. Meaning I would like 3 buttons below video that when clicked can redirect viewer to that area. (See file)
In the example I provided I am not set on shapes or colors, I want you to be creative.

See Fenwick Savings (the tabs at top are deals, coupons, stores)
See Quillboard told me to for aesthetics

I do not want bland or white background.

This site is all about consolidating the best offers for these 3 categories from across the internet. It is very connected to mobile functionality and making your smart phone work smartly for you to save money.
Updates

I just guaranteed payment for this project.

Industry/Entity Type

Retail

```html
<!DOCTYPE html>
<html lang="en">
<head>
<meta charset="utf-8">
<title>Offers of the Week</title>
<link rel="stylesheet" href="https://fonts.googleapis.com/css2?family=Ubuntu:wght@400;500&family=Arimo:wght@400;700&display=swap">
<style>
  :root {
    --bg-deep: #1e1712;
    --bg-warm: #3a2a1e;
    --header-dark: #1c1611;
    --panel: #2b3a4e;
    --accent: #6e9be2;
    --accent-soft: #7ba2e0;
    --link: #7aa7ea;
    --white: #ffffff;
    --rule: #d8d8d8;
    --circle: #e9eef0;
    --controls: #3c4250;
    --progress: #8dc21f;
    --volume: #2aa3dc;
  }
  * { box-sizing: border-box; margin: 0; padding: 0; }
  html, body { width: 1063px; height: 1200px; overflow: hidden; }
  body {
    position: relative;
    background: radial-gradient(ellipse at 50% 55%, var(--bg-warm) 0%, var(--bg-deep) 80%);
    font-family: "Ubuntu", sans-serif;
    color: var(--white);
  }
  .abs { position: absolute; }

  .site-header { left: 0; top: 0; width: 1063px; height: 107px; background: var(--header-dark); opacity: .92; }
  .brand { left: 96px; top: 18px; font-size: 28px; color: #4a9fe0; font-weight: 400; }
  .social-bar { left: 864px; top: 6px; width: 124px; height: 24px; background: #000; display: flex; gap: 6px; align-items: center; justify-content: center; }
  .social-bar span { width: 16px; height: 16px; background: var(--white); border-radius: 2px; }
  .main-nav { left: 355px; top: 76px; display: flex; gap: 28px; font-family: "Arimo", sans-serif; font-size: 16px; }
  .main-nav a { color: #5b86c6; text-decoration: none; letter-spacing: .3px; padding-bottom: 4px; }
  .main-nav a.active { color: #7ba6ec; border-bottom: 2px solid #7ba6ec; }

  .city-banner { left: 0; top: 107px; width: 1063px; height: 165px; background: linear-gradient(180deg, #6f7377 0%, #9a9c9e 55%, #7f8285 100%); }

  .search-panel { left: 70px; top: 228px; width: 944px; height: 88px; background: var(--panel); }
  .search-title { position: absolute; top: 4px; width: 100%; text-align: center; font-size: 25px; color: var(--accent); font-weight: 500; }
  .select { position: absolute; top: 44px; height: 38px; background: var(--white); border-radius: 3px; color: #222; font-family: "Arimo", sans-serif; font-size: 13px; padding: 11px 14px; }
  .select svg { position: absolute; right: 10px; top: 16px; }
  .search-button { position: absolute; left: 755px; top: 44px; width: 165px; height: 38px; background: var(--accent-soft); border-radius: 3px; text-align: center; line-height: 38px; font-size: 15px; font-weight: 500; }

  .video { left: 107px; top: 346px; width: 447px; height: 330px; border-radius: 3px; overflow: hidden; }
  .video-still { width: 447px; height: 284px; background: radial-gradient(ellipse at 60% 55%, #b7c68c 0%, #9a7d5e 40%, #6f4a3a 100%); }
  .video-controls { position: relative; height: 46px; background: var(--controls); }

  .welcome { left: 597px; top: 349px; width: 398px; height: 249px; background: var(--panel); }
  .welcome h2 { font-family: "Arimo", sans-serif; font-weight: 700; font-size: 28px; text-align: center; margin-top: 0; letter-spacing: -.5px; }
  .welcome p { font-family: "Arimo", sans-serif; font-size: 16px; line-height: 24.5px; text-align: justify; padding: 0 7px; margin-top: 29px; }
  .read-more { position: absolute; left: 250px; top: 194px; width: 123px; height: 41px; background: var(--accent-soft); border-bottom: 2px solid #c35a8a; text-align: center; line-height: 40px; font-size: 18px; }

  .category-switch { left: 588px; top: 614px; width: 416px; height: 59px; background: var(--panel); border-radius: 30px; display: flex; font-family: "Arimo", sans-serif; }
  .category-switch a { color: var(--white); text-decoration: none; display: flex; align-items: center; justify-content: center; font-size: 20px; }
  .category-switch a + a { border-left: 1px solid #55657a; }

  .divider { left: 70px; top: 711px; width: 943px; height: 1px; background: var(--rule); }
  .explore-title { left: 0; top: 733px; width: 1094px; text-align: center; font-size: 27px; color: var(--accent); font-weight: 500; }

  .see-all { width: 154px; height: 154px; border-radius: 50%; background: var(--circle); color: var(--link); display: flex; align-items: center; justify-content: center; text-align: center; font-size: 15px; line-height: 19px; }
  .vline { width: 2px; height: 228px; top: 815px; background: var(--white); }
  .place-list { list-style: none; font-family: "Arimo", sans-serif; font-size: 12px; line-height: 19.1px; color: var(--link); }
  .place-list.right { text-align: right; }
  .uk-map { left: 475px; top: 796px; width: 153px; height: 254px; background: radial-gradient(ellipse at 55% 60%, #86aaea 0%, #6f97dd 70%, rgba(111,151,221,0) 72%); border-radius: 40% 45% 40% 50%; }

  .site-footer { left: 46px; top: 1109px; width: 993px; height: 48px; background: var(--panel); text-align: center; line-height: 48px; font-size: 11px; }
</style>
</head>
<body>
  <header class="abs site-header"></header>
  <div class="abs brand">Company name/logo</div>
  <div class="abs social-bar" aria-label="Social links"><span></span><span></span><span></span><span></span><span></span></div>
  <nav class="abs main-nav">
    <a class="active" href="#">ALL POSTS</a><a href="#">RETAIL</a><a href="#">GROCERY</a><a href="#">RESTAURANT</a>
  </nav>

  <div class="abs city-banner" role="img" aria-label="Greyscale city skyline with tall buildings"></div>

  <section class="abs search-panel">
    <h2 class="search-title">Search Offers</h2>
    <div class="select" style="left:49px;width:233px">Select Retail<svg width="11" height="7"><path d="M0 0h11L5.5 7z" fill="#6e9be2"/></svg></div>
    <div class="select" style="left:285px;width:234px">Select Grocery<svg width="11" height="7"><path d="M0 0h11L5.5 7z" fill="#6e9be2"/></svg></div>
    <div class="select" style="left:520px;width:233px">Select Restaurant<svg width="11" height="7"><path d="M0 0h11L5.5 7z" fill="#6e9be2"/></svg></div>
    <div class="search-button">Search</div>
  </section>

  <div class="abs video">
    <div class="video-still" role="img" aria-label="Video still of a green coffee cup on a saucer with coffee beans on a table"></div>
    <div class="video-controls">
      <svg width="447" height="46">
        <rect x="14" y="15" width="4" height="16" fill="#fff"/><rect x="22" y="15" width="4" height="16" fill="#fff"/>
        <rect x="45" y="21" width="215" height="5" rx="2" fill="#2a2e37"/>
        <rect x="45" y="21" width="130" height="5" rx="2" fill="var(--progress)"/>
        <rect x="175" y="21" width="45" height="5" fill="#5a6070"/>
        <circle cx="175" cy="23.5" r="6.5" fill="#fff"/>
        <text x="265" y="28" fill="#fff" font-family="Arimo, sans-serif" font-size="13" font-weight="700">12:04</text>
        <path d="M317 19h4l5-4v17l-5-4h-4z" fill="#2a2e37"/>
        <rect x="340" y="21" width="50" height="5" rx="2" fill="var(--volume)"/>
        <circle cx="390" cy="23.5" r="6.5" fill="#fff"/>
        <path d="M412 20v-6h6M428 14h6v6M434 28v6h-6M418 34h-6v-6" stroke="#fff" stroke-width="2.5" fill="none"/>
        <rect x="417" y="19" width="12" height="10" fill="#fff"/>
      </svg>
    </div>
  </div>

  <section class="abs welcome">
    <h2>Welcome</h2>
    <p>Lorem ipsum dolor sit amet, consectetur adipiscing elit. Mauris quis aliquet purus, vitae rhoncus mauris. Sed egestas erat a lectus mollis, viverra pretium magna tempus. Nunc mi quam, porta nec accumsan</p>
    <div class="read-more">Readmore</div>
  </section>

  <nav class="abs category-switch">
    <a href="#" style="width:140px">RETAIL</a>
    <a href="#" style="width:137px">GROCERY</a>
    <a href="#" style="width:139px;font-size:17px">RESTAURANT</a>
  </nav>

  <div class="abs divider"></div>
  <h2 class="abs explore-title">Explore by location</h2>

  <div class="abs see-all" style="left:91px;top:852px">See All<br>Locations</div>
  <div class="abs vline" style="left:294px"></div>
  <ul class="abs place-list" style="left:324px;top:825px">
    <li>England - London</li><li>East Midlands</li><li>North</li><li>North East</li><li>North West</li><li>South East</li><li>South West</li><li>West Midlands</li><li>Wales - East</li><li>Wales - North</li><li>Wales - South</li>
  </ul>
  <div class="abs uk-map" role="img" aria-label="Map of the United Kingdom"></div>
  <ul class="abs place-list right" style="left:660px;top:825px;width:114px">
    <li>Cheshire</li><li>Essex</li><li>Hampshire</li><li>Hertfordshire</li><li>Kent</li><li>Lancashire</li><li>Leicestershire</li><li>London</li><li>Surrey</li><li>Cornwall</li><li>Devon</li>
  </ul>
  <div class="abs vline" style="left:804px"></div>
  <div class="abs see-all" style="left:842px;top:852px">See All<br>Counties</div>

  <footer class="abs site-footer">Copyright © 2014. All rights reserved</footer>
</body>
</html>
```